We need a refreshed business card. Our company is a venture capital investment firm focused on investing in medical devices. Logo is attached. please also see our website www.velmoracapital.example

Target Market(s)

investors and potential investment targets

Industry/Entity Type

medical investments

Contact Information for Business Card

logo, name, title, email, phone, website, address,

Colors
0054AA
0677BA
7BADD7
CADEEF
E8F1F8
0094D4
00A9DD
6FCCEA
C7EBF8
E9F6FB
00AB8E
00BBA5
67D7C9
C6EFE9
E9F9F6

Requirements
Must have
• fresh modern design
Nice to have
• QR code leading to our linked in page, short description of what we do “Early Stage Medical Device Investors”

```html
<!DOCTYPE html>
<html lang="en">
<head>
<meta charset="utf-8">
<title>Velmora Business Card</title>
<link rel="stylesheet" href="https://fonts.googleapis.com/css2?family=Montserrat:wght@600;700&family=Nunito+Sans:wght@400;600&display=swap">
<style>
  :root {
    --blue: #0054AA;
    --teal: #00AB8E;
    --ink: #1d1d1f;
    --white: #ffffff;
    --backdrop: #b9b9b9;
  }
  * { margin: 0; padding: 0; box-sizing: border-box; }
  html, body { width: 1200px; height: 1200px; overflow: hidden; }
  body {
    background: var(--backdrop);
    font-family: "Nunito Sans", Arial, sans-serif;
    color: var(--ink);
    position: relative;
  }
  .card {
    position: absolute;
    left: 227px;
    width: 746px;
    height: 428px;
    overflow: hidden;
  }
  .card--front { top: 113px; background: var(--white); }
  .card--back { top: 582px; background: var(--teal); }

  .front-wave { position: absolute; inset: 0; width: 100%; height: 100%; }

  .contact-block { position: absolute; left: 28px; top: 86px; }
  .person-name {
    font-family: "Montserrat", Arial, sans-serif;
    font-weight: 700;
    font-size: 28px;
    letter-spacing: -0.2px;
    line-height: 1;
  }
  .person-name .given { color: var(--blue); }
  .person-name .family { color: var(--teal); }
  .person-title { font-size: 19px; margin-top: 8px; }
  .address { font-size: 19px; line-height: 27px; margin-top: 22px; }
  .contact-list { list-style: none; margin-top: 20px; }
  .contact-list li {
    display: flex; align-items: center;
    font-size: 19px; height: 30px;
  }
  .contact-list svg { width: 16px; height: 16px; margin-right: 14px; flex: none; }

  .brand-name {
    position: absolute;
    font-family: "Montserrat", Arial, sans-serif;
    font-weight: 600;
    line-height: 1;
  }
  .card--front .brand-name {
    right: 60px; top: 146px;
    font-size: 58px; color: var(--blue);
  }
  .card--back .brand-name {
    left: 0; right: 0; top: 165px;
    text-align: center;
    font-size: 96px; color: var(--white);
  }
</style>
</head>
<body>
  <section class="card card--front">
    <svg class="front-wave" viewBox="0 0 746 428" preserveAspectRatio="none" aria-hidden="true">
      <path d="M0,410 Q430,402 746,254 L746,428 L0,428 Z" fill="var(--teal)"/>
      <path d="M0,383 Q410,428 712,272 Q420,412 0,399 Z" fill="var(--blue)"/>
    </svg>

    <div class="contact-block">
      <h1 class="person-name"><span class="given">DARA</span> <span class="family">WHITLOCK</span></h1>
      <p class="person-title">Managing Director</p>
      <p class="address">Harbor Point 2200 Linden<br>Ave Suite 310</p>
      <ul class="contact-list">
        <li>
          <svg viewBox="0 0 16 16"><path d="M3.5 1.5l2.5 2.8-1.4 1.9c.9 2 2.5 3.6 4.6 4.6l1.9-1.4 2.8 2.5-1.3 2.1C7.5 14.3 1.7 8.5 1.4 2.8z" fill="var(--teal)"/></svg>
          +61 400 555 019
        </li>
        <li>
          <svg viewBox="0 0 16 16"><rect x="1" y="3.5" width="14" height="9" fill="var(--teal)"/><path d="M1.5 4l6.5 5 6.5-5" fill="none" stroke="var(--white)" stroke-width="1.2"/></svg>
          info@velmoracapital.example
        </li>
        <li>
          <svg viewBox="0 0 16 16"><circle cx="8" cy="8" r="7" fill="var(--teal)"/><path d="M1 8h14M8 1c-3 3-3 11 0 14M8 1c3 3 3 11 0 14" fill="none" stroke="var(--white)" stroke-width="0.9"/></svg>
          www.velmoracapital.example
        </li>
      </ul>
    </div>

    <p class="brand-name">Velmora</p>
  </section>

  <section class="card card--back">
    <p class="brand-name">Velmora</p>
  </section>
</body>
</html>
```